Business Cards for Life Coaching Practice
RVT Harbor Ltd
Business Cards for Life Coaching Practice - Consulting
Creative Brief
Professional
Dovinder Plume
admin@rvtharbor.co.uk
brightpathmentoring.co.uk
Please show me both 1 side and 2 sided options. I have uploaded logo files and would like to see design options using the colour schemes.
"Be True To Yourself" ------Your Journey-------
RVTHARBOR RVTHARBOR
please only send me designs on plastic cards.
sevensky sevensky
Its Done! check your private messages on top right side messages (1) thanks!
#33 please can you provide different colour backgrounds for this design?
Its Done! thanks
#32 Please apply this back to designs #23 - #25 and #27 - #29
#22 the blue stone is too big for the card and needs to be smaller to fit on the card
#14 I like the plastic shine type card. As stated i would like the statement on back and stones need to be on card
#7 I like the wave concept. The back is however too dark and I want "be true to yourself" on the back.

```html
<!DOCTYPE html>
<html lang="en">
<head>
<meta charset="utf-8">
<title>RVT Harbor Ltd – Business Cards</title>
<link href="https://fonts.googleapis.com/css2?family=Cinzel:wght@400;600&display=swap" rel="stylesheet">
<style>
  :root {
    --backdrop: #d8d9da;
    --card: #ffffff;
    --brand-blue: #1f5fa8;
    --wave-blue: #1d63b3;
    --wave-grey: #8ea4aa;
    --teal: #3a8fa6;
    --ink: #4a4f55;
    --rule: #9aa3a8;
    --shadow: rgba(0,0,0,0.18);
  }
  * { margin: 0; padding: 0; box-sizing: border-box; }
  html, body { width: 1200px; height: 987px; overflow: hidden; }
  body {
    background: var(--backdrop);
    font-family: "Cinzel", "Times New Roman", serif;
    color: var(--ink);
    position: relative;
  }
  .card {
    position: absolute;
    left: 250px;
    width: 700px;
    height: 437px;
    background: var(--card);
    border-radius: 24px;
    box-shadow: 0 10px 26px var(--shadow);
    overflow: hidden;
  }
  .card--back { top: 36px; }
  .card--front { top: 510px; }

  .brand {
    position: absolute;
    display: flex;
    align-items: center;
    gap: 14px;
  }
  .brand__dot {
    width: 40px; height: 40px; border-radius: 50%;
    background: var(--teal);
    flex: none;
  }
  .brand__name {
    font-size: 36px;
    font-weight: 600;
    color: var(--brand-blue);
    letter-spacing: 1px;
    white-space: nowrap;
  }
  .frame-line {
    position: absolute;
    border-top: 1px dashed var(--rule);
  }

  .card--back .brand { left: 0; right: 0; top: 190px; justify-content: center; }
  .card--back .frame-line { left: 190px; top: 170px; width: 320px; border-left: 1px dashed var(--rule); height: 80px; }

  .card--front .brand { left: 0; right: 0; top: 62px; justify-content: center; }
  .card--front .frame-line { left: 170px; top: 42px; width: 360px; }

  .contact-left {
    position: absolute;
    right: 370px;
    top: 186px;
    text-align: right;
  }
  .website { font-size: 12px; letter-spacing: 0.5px; color: var(--ink); }
  .person {
    font-size: 19px; font-weight: 600; color: var(--brand-blue);
    margin-top: 22px; letter-spacing: 0.5px;
  }
  .divider {
    position: absolute; left: 344px; top: 176px;
    width: 1px; height: 90px; background: var(--rule);
  }
  .contact-right {
    position: absolute; left: 358px; top: 182px;
    list-style: none;
  }
  .contact-right li {
    display: flex; align-items: center; gap: 8px;
    font-size: 13px; margin-bottom: 8px; letter-spacing: 0.5px;
    white-space: nowrap;
  }
  .contact-right svg { width: 16px; height: 16px; flex: none; }
  .waves { position: absolute; left: 0; bottom: 0; width: 700px; height: 437px; }
</style>
</head>
<body>

  <section class="card card--back" aria-label="Card back">
    <div class="frame-line"></div>
    <div class="brand">
      <span class="brand__dot"></span>
      <span class="brand__name">RVT Harbor</span>
    </div>
  </section>

  <section class="card card--front" aria-label="Card front">
    <svg class="waves" viewBox="0 0 700 437" preserveAspectRatio="none" aria-hidden="true">
      <path d="M0,292 C200,318 410,420 700,370 L700,437 L0,437 Z" fill="var(--wave-grey)"/>
      <path d="M0,322 C220,342 420,432 700,386 L700,437 L0,437 Z" fill="#ffffff"/>
      <path d="M0,338 C220,356 420,444 700,398 L700,437 L0,437 Z" fill="var(--wave-blue)"/>
    </svg>

    <div class="frame-line"></div>
    <div class="brand">
      <span class="brand__dot"></span>
      <span class="brand__name">RVT Harbor</span>
    </div>

    <div class="contact-left">
      <p class="website">www.brightpathmentoring.co.uk</p>
      <p class="person">Dovinder Plume</p>
    </div>
    <div class="divider"></div>
    <ul class="contact-right">
      <li>
        <svg viewBox="0 0 16 16"><circle cx="8" cy="8" r="8" fill="var(--brand-blue)"/><path d="M5.5,4 l1.5,0 l.6,2 l-1,.8 a5,5 0 0 0 2.6,2.6 l.8,-1 l2,.6 l0,1.5 a1,1 0 0 1 -1,1 a7,7 0 0 1 -6.5,-6.5 a1,1 0 0 1 1,-1 z" fill="#fff"/></svg>
        020-7946-0381
      </li>
      <li>
        <svg viewBox="0 0 16 16"><circle cx="8" cy="8" r="8" fill="var(--brand-blue)"/><rect x="5.5" y="3.5" width="5" height="9" rx="1" fill="#fff"/><rect x="6.5" y="4.8" width="3" height="5.5" fill="var(--brand-blue)"/></svg>
        123-456-7890
      </li>
      <li>
        <svg viewBox="0 0 16 16"><circle cx="8" cy="8" r="8" fill="var(--brand-blue)"/><rect x="4" y="5" width="8" height="6" fill="#fff"/><path d="M4,5 L8,8.5 L12,5" fill="none" stroke="var(--brand-blue)" stroke-width="0.8"/></svg>
        admin@rvtharbor.co.uk
      </li>
    </ul>
  </section>

</body>
</html>
```